We need a Glass-Shattering Brochure

We area start up renewable company based in the UK but operate in West Africa. We have a unique blend of local know-how and international exposure to latest solar technology. We pride ourselves in bringing next generation, ground breaking, value for money solar products to Africa.

We are launching a massive campaign to introduce some of the world's best solar product to our high net-worth clients and decision makers. This will be a single brochure of A4 size on 8 pages. Details of the page content is attached.

Also a sample of what we like is attached. The brochure must be clean , fresh, very contemporary and straight to the point - Clear

I have attached a link to some of our installation pictures and some pictures that I think you might need. But feel free to source pictures you think will be appropriate for the intended audience.

You can access some of our paid pictures and installation pictures here https://filedrop-example.net/f/x7KpQm2RtLw9ZvNc4HdYs8BjE

Apologies to everyone. We have just uploaded the brochure content

Target Market(s)

Top company executives

Industry/Entity Type

It Company

Requirements
Must have
• Similar font used in the sample brochure attached. White background. Hint of the green. Please check out our website at www.tolvarpower.co.uk
Nice to have
• Other pictures other than the ones provided

```html
<!DOCTYPE html>
<html lang="en">
<head>
<meta charset="utf-8">
<title>Tolvar Power Brochure Cover</title>
<link rel="stylesheet" href="https://fonts.googleapis.com/css2?family=Bebas+Neue&family=Oswald:wght@500&family=Lato:wght@400;700&display=swap">
<style>
  :root {
    --bg: #e4e4e4;
    --paper: #ffffff;
    --green-bright: #5cc43a;
    --green-deep: #137a34;
    --ink: #2b2b2b;
    --ink-soft: #3a3a3a;
    --rule-red: #c9383a;
  }
  * { box-sizing: border-box; margin: 0; padding: 0; }
  html, body { width: 1200px; height: 1200px; overflow: hidden; }
  body { background: var(--bg); font-family: "Lato", sans-serif; }
  .canvas { position: relative; width: 1200px; height: 1200px; }
  .page {
    position: absolute; top: 246px; width: 500px; height: 707px;
    background: var(--paper); overflow: hidden;
    box-shadow: 0 6px 18px rgba(0,0,0,0.18);
  }
  .page--front { left: 70px; }
  .page--back { left: 630px; }
  .page svg { position: absolute; inset: 0; width: 500px; height: 707px; }
  .brand {
    position: absolute; left: 0; right: 0; display: flex;
    justify-content: center; align-items: center; gap: 10px;
  }
  .brand__dot { width: 36px; height: 36px; border-radius: 50%; background: var(--green-bright); }
  .brand__name {
    font-family: "Lato", sans-serif; font-weight: 700; font-size: 27px;
    color: var(--ink); letter-spacing: 0.5px;
  }
  .page--front .brand { top: 48px; }
  .page--back .brand { top: 76px; }
  .headline {
    position: absolute; left: 0; right: 0; top: 502px; text-align: center;
    font-family: "Bebas Neue", sans-serif; font-size: 56px; line-height: 1;
    color: var(--green-bright); letter-spacing: 0.5px;
  }
  .tagline {
    position: absolute; left: 0; right: 0; top: 564px; text-align: center;
    font-family: "Oswald", sans-serif; font-weight: 500; font-size: 16px;
    color: var(--ink); letter-spacing: -0.2px;
  }
  .web {
    position: absolute; left: 0; right: 0; text-align: center;
    font-family: "Lato", sans-serif; font-size: 16px; letter-spacing: 3.5px;
  }
  .page--front .web { top: 597px; color: var(--ink-soft); }
  .page--back .web { top: 388px; color: var(--green-bright); }
  .address {
    position: absolute; left: 0; right: 0; top: 318px; text-align: center;
    font-size: 14px; line-height: 1.3; color: var(--ink);
  }
</style>
</head>
<body>
<div class="canvas">

  <!-- Front cover -->
  <section class="page page--front">
    <svg viewBox="0 0 500 707" aria-hidden="false">
      <defs>
        <linearGradient id="familyTone" x1="0" y1="0" x2="1" y2="1">
          <stop offset="0" stop-color="#ece7e2"/>
          <stop offset="0.5" stop-color="#8a5f48"/>
          <stop offset="1" stop-color="#8c8f96"/>
        </linearGradient>
        <linearGradient id="equipTone" x1="0" y1="0" x2="1" y2="1">
          <stop offset="0" stop-color="#eeeeee"/>
          <stop offset="0.6" stop-color="#e98a3c"/>
          <stop offset="1" stop-color="#5a6b80"/>
        </linearGradient>
      </defs>
      <g role="img" aria-label="Photo of a smiling family watching television together at home">
        <path d="M0,205 C30,172 60,152 85,140 C92,172 120,156 170,150 C300,140 420,122 500,55 L500,412 C430,424 330,424 268,458 L0,458 Z" fill="url(#familyTone)"/>
      </g>
      <path d="M0,205 C30,172 60,152 85,140 C92,172 120,156 170,150 C300,140 420,122 500,55" fill="none" stroke="var(--green-bright)" stroke-width="9"/>
      <path d="M0,199 C30,166 60,146 83,134 C90,165 120,150 170,144 C300,134 420,116 500,49" fill="none" stroke="#1b1b1b" stroke-width="1.2"/>
      <path d="M500,412 C430,424 330,424 268,458" fill="none" stroke="var(--green-bright)" stroke-width="8"/>
      <circle cx="130" cy="355" r="104" fill="#1b1b1b"/>
      <circle cx="130" cy="355" r="102" fill="var(--green-bright)"/>
      <g role="img" aria-label="Photo of wall-mounted orange solar inverters">
        <circle cx="130" cy="355" r="94" fill="url(#equipTone)"/>
      </g>
      <path d="M0,650 C150,690 340,650 500,598 L500,707 L0,707 Z" fill="var(--green-deep)"/>
      <path d="M0,640 C150,676 340,640 500,586" fill="none" stroke="var(--green-bright)" stroke-width="6"/>
      <path d="M0,633 C150,668 340,632 500,578" fill="none" stroke="#1b1b1b" stroke-width="1.5"/>
    </svg>
    <div class="brand"><span class="brand__dot"></span><span class="brand__name">TOLVAR POWER</span></div>
    <h1 class="headline">LETS DO THE IMPOSSIBLE !</h1>
    <p class="tagline">SYSTEM SOLUTIONS FOR RELIABLE OFF-GRID POWER SUPPLY</p>
    <p class="web">www.tolvarpower.co.uk</p>
  </section>

  <!-- Back cover -->
  <section class="page page--back">
    <svg viewBox="0 0 500 707">
      <defs>
        <linearGradient id="panelTone" x1="0" y1="0" x2="0" y2="1">
          <stop offset="0" stop-color="#f2f2f2"/>
          <stop offset="1" stop-color="#e6e6e6"/>
        </linearGradient>
        <linearGradient id="paperShade" x1="0" y1="0" x2="1" y2="1">
          <stop offset="0" stop-color="#ffffff"/>
          <stop offset="1" stop-color="#ececec"/>
        </linearGradient>
        <linearGradient id="houseTone" x1="0" y1="0" x2="0" y2="1">
          <stop offset="0" stop-color="#bcd6ee"/>
          <stop offset="0.5" stop-color="#e9e9e6"/>
          <stop offset="1" stop-color="#9fb57a"/>
        </linearGradient>
        <linearGradient id="roofTone" x1="0" y1="0" x2="0" y2="1">
          <stop offset="0" stop-color="#8fc2ea"/>
          <stop offset="0.45" stop-color="#d2764e"/>
          <stop offset="1" stop-color="#2e3e66"/>
        </linearGradient>
        <linearGradient id="installTone" x1="0" y1="0" x2="1" y2="1">
          <stop offset="0" stop-color="#a9cdea"/>
          <stop offset="0.5" stop-color="#2b2f38"/>
          <stop offset="1" stop-color="#3e5fa0"/>
        </linearGradient>
      </defs>
      <g role="img" aria-label="Faint photo of electrical meter boxes on a wall">
        <rect x="0" y="0" width="500" height="440" fill="url(#panelTone)"/>
      </g>
      <path d="M0,240 C60,195 200,205 290,195 C330,190 345,180 358,168 C360,260 430,330 500,405 L500,707 L0,707 Z" fill="url(#paperShade)"/>
      <path d="M0,240 C60,195 200,205 290,195 C330,190 345,180 358,168 C360,260 430,330 500,405" fill="none" stroke="var(--green-bright)" stroke-width="9"/>
      <path d="M0,234 C60,189 200,199 290,189 C328,184 345,174 360,160" fill="none" stroke="#1b1b1b" stroke-width="1.2"/>
      <circle cx="104" cy="536" r="68" fill="#1b1b1b"/>
      <circle cx="104" cy="536" r="66" fill="var(--green-bright)"/>
      <g role="img" aria-label="Illustration of a house with rooftop solar panels">
        <circle cx="104" cy="536" r="59" fill="url(#houseTone)"/>
      </g>
      <circle cx="389" cy="536" r="66" fill="#1b1b1b"/>
      <circle cx="389" cy="536" r="64" fill="var(--green-bright)"/>
      <g role="img" aria-label="Photo of a technician installing solar panels on a roof">
        <circle cx="389" cy="536" r="57" fill="url(#installTone)"/>
      </g>
      <circle cx="243" cy="536" r="84" fill="#1b1b1b"/>
      <circle cx="243" cy="536" r="82" fill="var(--green-bright)"/>
      <g role="img" aria-label="Photo of a yellow house with solar panels on its roof">
        <circle cx="243" cy="536" r="74" fill="url(#roofTone)"/>
      </g>
      <path d="M0,650 C150,690 340,650 500,598 L500,707 L0,707 Z" fill="var(--green-deep)"/>
      <path d="M0,640 C150,676 340,640 500,586" fill="none" stroke="var(--green-bright)" stroke-width="6"/>
      <path d="M0,633 C150,668 340,632 500,578" fill="none" stroke="#1b1b1b" stroke-width="1.5"/>
    </svg>
    <div class="brand"><span class="brand__dot"></span><span class="brand__name">TOLVAR POWER</span></div>
    <address class="address" style="font-style:normal">3rd Floor, Plot 12, Block 58,<br>Adeyemi Lawson Crescent, Lekki,<br>Lagos, Nigeria</address>
    <p class="web">www.tolvarpower.co.uk</p>
  </section>

</div>
</body>
</html>
```